Business card design needed

We are 2 artists starting up a studio by the water in Sydney ...where we can work and display our art...would like the back ground to be Navy and white stripe...nautical...and the name The Clay Nook to be bold and the main wording...not nautical...if possible thought the A for art could be an easel ...ie the capital A using the cross bar as the platform that paint would be circles of colour....would like the main wording in Black but the easel A in colour
Hope u are able to help
thanku Lorna Vesk
as I will be away in a week for 4 weeks could u please send all info to Jodie Minchens email....she can contact me and we can go ahead asap....

Industry/Entity Type

Artists

Contact Information for Business Card

THE CLAY NOOK

Halloways Dock House
The Bend..41 Kelvane Rd..Corvale 2199 Harbourton

Jodi Minchen..0417583091..jodiminchen@mailwave.example
Lorn Vesk...0413862714..lvesk@quillnet.example.au

```html
<!DOCTYPE html>
<html lang="en">
<head>
<meta charset="utf-8">
<title>The Clay Nook – Business Card</title>
<link rel="stylesheet" href="https://fonts.googleapis.com/css2?family=Arimo:wght@400;700&display=swap">
<style>
  :root {
    --stripe-top: #544673;
    --stripe-bottom: #2f2a4b;
    --navy: #2d2d4a;
    --paper: #ffffff;
    --ink-light: #ffffff;
    --brand-red: #e8323c;
    --edge: #d8d8dc;
  }
  html, body {
    margin: 0;
    padding: 0;
    overflow: hidden;
    background: var(--paper);
  }
  .card {
    position: relative;
    width: 1200px;
    height: 677px;
    background: var(--paper);
    overflow: hidden;
    box-shadow: inset 0 0 0 1px var(--edge);
    font-family: "Arimo", Arial, sans-serif;
  }
  .stripe {
    position: absolute;
    left: 4px;
    right: 4px;
    height: 37px;
    background: linear-gradient(to bottom, var(--stripe-top), var(--stripe-bottom));
  }
  .stripe--1 { top: 31px; }
  .stripe--2 { top: 100px; }
  .stripe--3 { top: 169px; }
  .stripe--4 { top: 236px; }
  .stripe--5 { top: 303px; }
  .stripe--6 { top: 369px; }

  .brand-panel {
    position: absolute;
    left: 724px;
    top: 78px;
    width: 405px;
    height: 320px;
    background: var(--paper);
    border-radius: 12px;
    box-shadow: 0 10px 18px rgba(0,0,0,0.35), 0 0 0 1px rgba(0,0,0,0.06);
    display: flex;
    align-items: center;
    justify-content: center;
  }
  .brand-name {
    margin: 0;
    font-weight: 400;
    font-size: 66px;
    line-height: 1.05;
    letter-spacing: 1px;
    color: var(--brand-red);
    text-align: left;
  }

  .info-band {
    position: absolute;
    left: 4px;
    right: 4px;
    top: 434px;
    bottom: 4px;
    background: var(--navy);
    color: var(--ink-light);
  }
  .studio-details,
  .contact-details {
    position: absolute;
    margin: 0;
    font-size: 26px;
    line-height: 33.5px;
    font-style: normal;
  }
  .studio-details { left: 52px; top: 48px; }
  .contact-details { left: 729px; top: 42px; }
  .details-heading {
    display: block;
    font-weight: 700;
  }
</style>
</head>
<body>
  <main class="card">
    <div class="stripe stripe--1"></div>
    <div class="stripe stripe--2"></div>
    <div class="stripe stripe--3"></div>
    <div class="stripe stripe--4"></div>
    <div class="stripe stripe--5"></div>
    <div class="stripe stripe--6"></div>

    <div class="brand-panel">
      <h1 class="brand-name">The Clay<br>Nook</h1>
    </div>

    <section class="info-band">
      <address class="studio-details">
        <span class="details-heading">THE CLAY NOOK</span>
        Halloways Dock House The Bend.<br>
        41 Kelvane Rd.<br>
        Corvale 2199 Harbourton Jodi Minchen 0417583091
      </address>
      <address class="contact-details">
        <span class="details-heading">Lorn Vesk</span>
        jodiminchen@mailwave.example<br>
        0413862714<br>
        lvesk@quillnet.example.au
      </address>
    </section>
  </main>
</body>
</html>
```